Create a new business card

I’m looking to update my business card to make it match the rest of my brand. I will include my current website as well as what my vehicle designs look like, etc..
What my business currently services
Weekly maintenance pool openings / closings
Equipment repair, including pumps, heaters, salt systems, filters, etc.
We install automatic covers and maintain them as well as provide preventative maintenance

I would like to include my name.
Bradley Kessner.
My title
Owner
My email
Brad@wavecrewnx.com
5079164826
Www.wavecrewnx.com

```html
<!DOCTYPE html>
<html lang="en">
<head>
<meta charset="utf-8">
<title>Wave Crew Pools – Business Card</title>
<link href="https://fonts.googleapis.com/css2?family=Montserrat:wght@400;500;600;700&display=swap" rel="stylesheet">
<style>
  :root {
    --bg: #24262b;
    --navy: #1f3a78;
    --deep-blue: #234c94;
    --sky: #3fb3e8;
    --sky-light: #45aee6;
    --orange: #e25a1c;
    --white: #ffffff;
    --ink: #1c1c1c;
  }
  * { box-sizing: border-box; margin: 0; padding: 0; }
  html, body { width: 1200px; height: 900px; overflow: hidden; }
  body {
    background: var(--bg);
    font-family: "Montserrat", sans-serif;
    position: relative;
  }
  .card {
    position: absolute;
    width: 600px;
    height: 343px;
    border-radius: 22px;
    overflow: hidden;
    box-shadow: 0 14px 30px rgba(0,0,0,.45);
  }
  /* Services side */
  .card-services {
    left: 300px; top: 70px;
    background: linear-gradient(30deg, var(--sky) 0%, #2f86c8 45%, var(--navy) 100%);
    color: var(--white);
  }
  .brand-mark {
    position: absolute;
    display: flex; align-items: center; gap: 14px;
  }
  .brand-dot {
    width: 34px; height: 34px; border-radius: 50%;
    background: currentColor;
    flex: none;
  }
  .brand-name {
    font-weight: 700;
    font-size: 26px;
    line-height: 1.1;
  }
  .card-services .brand-mark { left: 48px; top: 140px; color: var(--white); }
  .divider {
    position: absolute;
    left: 300px; top: 60px;
    width: 1px; height: 220px;
    background: rgba(255,255,255,.55);
  }
  .services {
    position: absolute;
    left: 325px; top: 62px;
  }
  .services-title {
    color: var(--sky-light);
    font-weight: 700;
    font-size: 22px;
    letter-spacing: .5px;
    margin-bottom: 10px;
  }
  .services-list { list-style: none; }
  .services-list li {
    font-size: 14px;
    line-height: 1.75;
    padding-left: 12px;
    position: relative;
  }
  .services-list li::before {
    content: "";
    position: absolute; left: 0; top: 10px;
    width: 5px; height: 5px; border-radius: 50%;
    background: var(--white);
  }
  /* Contact side */
  .card-contact {
    left: 300px; top: 487px;
    background: var(--white);
  }
  .wave { position: absolute; inset: 0; }
  .card-contact .brand-mark { right: 40px; top: 48px; color: var(--navy); }
  .person {
    position: absolute;
    left: 42px; top: 140px;
  }
  .person-name {
    color: var(--sky-light);
    font-weight: 700;
    font-size: 28px;
  }
  .person-title {
    color: var(--ink);
    font-size: 15px;
    margin-top: 2px;
  }
  .contacts {
    position: absolute;
    left: 250px; top: 230px;
    list-style: none;
    color: var(--white);
  }
  .contacts li {
    display: flex; align-items: center; gap: 12px;
    font-size: 15px;
    height: 28px;
  }
  .icon {
    width: 20px; height: 20px;
    border-radius: 5px;
    background: var(--sky-light);
    display: flex; align-items: center; justify-content: center;
    flex: none;
  }
  .icon svg { width: 12px; height: 12px; }
</style>
</head>
<body>

<section class="card card-services">
  <div class="brand-mark">
    <span class="brand-dot"></span>
    <span class="brand-name">Wave Crew<br>Pools</span>
  </div>
  <div class="divider"></div>
  <div class="services">
    <h2 class="services-title">OUR SERVICES</h2>
    <ul class="services-list">
      <li>Pool Opening and Closing</li>
      <li>Renovation</li>
      <li>Weekly pool services</li>
      <li>Electronic Leak detection</li>
      <li>Structural Pool Repair</li>
      <li>Equipment repairs and Upgrades</li>
    </ul>
  </div>
</section>

<section class="card card-contact">
  <svg class="wave" viewBox="0 0 600 343" preserveAspectRatio="none" aria-hidden="true">
    <defs>
      <linearGradient id="waveBlue" x1="0" y1="1" x2="1" y2="0">
        <stop offset="0" stop-color="#1f3a78"/>
        <stop offset=".55" stop-color="#2f7cc4"/>
        <stop offset="1" stop-color="#45b4ea"/>
      </linearGradient>
    </defs>
    <path d="M92,343 C160,230 250,178 380,164 C480,152 560,130 600,80 L600,343 Z" fill="#e25a1c"/>
    <path d="M112,343 C180,236 265,190 385,176 C485,164 560,144 600,104 L600,343 Z" fill="#ffffff"/>
    <path d="M124,343 C190,244 275,200 390,186 C490,174 565,152 600,116 L600,343 Z" fill="url(#waveBlue)"/>
  </svg>

  <div class="brand-mark">
    <span class="brand-dot"></span>
    <span class="brand-name">Wave Crew<br>Pools</span>
  </div>

  <div class="person">
    <h1 class="person-name">Bradley Kessner</h1>
    <p class="person-title">Owner</p>
  </div>

  <ul class="contacts">
    <li>
      <span class="icon"><svg viewBox="0 0 12 12"><path d="M2.5 1h2l1 2.5-1.3 1a6 6 0 0 0 3.3 3.3l1-1.3L11 7.5v2A1.5 1.5 0 0 1 9.5 11 8.5 8.5 0 0 1 1 2.5 1.5 1.5 0 0 1 2.5 1z" fill="#fff"/></svg></span>
      5079164826
    </li>
    <li>
      <span class="icon"><svg viewBox="0 0 12 12"><rect x="1" y="2.5" width="10" height="7" rx="1" fill="#fff"/><path d="M1.5 3l4.5 3.5L10.5 3" stroke="#45aee6" fill="none"/></svg></span>
      Brad@wavecrewnx.com
    </li>
    <li>
      <span class="icon"><svg viewBox="0 0 12 12"><circle cx="6" cy="6" r="4.5" fill="none" stroke="#fff" stroke-width="1.2"/><path d="M1.5 6h9M6 1.5c-2 2.5-2 6.5 0 9M6 1.5c2 2.5 2 6.5 0 9" stroke="#fff" fill="none"/></svg></span>
      Www.wavecrewnx.com
    </li>
  </ul>
</section>

</body>
</html>
```